Kick The Pickle! Summer One Act Festival

I need a poster design for a summer festival of short comedy plays in San Francisco, all with a historical or intellectual theme! From Ancient Greece to the Russian Revolution to Cold War Politics to College Admissions! The target audience demographic is 20-30 year old San Francisco "hipster types" who will be attending a food truck festival. The festival performance dates are Friday evenings, July 22 to August 15! We would like a clever, antique looking design that conveys comedy and history. We would also like the names of the plays, all by the same author, Milo Tennant, on the poster as well! The titles are:

Tentaxi
Wine Without Dread
That Huge Dumb Gothic Epic
Tune Tickle
Freshman Fumbles
Somebody Wore a Hat

Festival

```html
<!DOCTYPE html>
<html lang="en">
<head>
<meta charset="utf-8">
<title>Kick The Pickle! Summer One Act Festival</title>
<link rel="stylesheet" href="https://fonts.googleapis.com/css2?family=Bebas+Neue&display=swap">
<style>
  :root {
    --page: #ffffff;
    --mount: #2e2e2e;
    --paper: #d4d0cc;
    --rule: #8c8986;
    --ink: #4a4a4a;
    --ink-soft: #6a6866;
    --art: #c4bfba;
  }
  * { margin: 0; padding: 0; box-sizing: border-box; }
  html, body {
    width: 1200px;
    height: 1000px;
    overflow: hidden;
    background: var(--page);
  }
  .canvas {
    position: relative;
    width: 1200px;
    height: 1000px;
  }
  .mount {
    position: absolute;
    left: 22px; top: 18px;
    width: 1158px; height: 962px;
    border: 4px solid var(--mount);
  }
  .poster {
    position: absolute;
    left: 268px; top: 55px;
    width: 688px; height: 890px;
    background: var(--paper);
    font-family: "Bebas Neue", "Oswald", sans-serif;
    color: var(--ink);
    text-align: center;
  }
  .poster-frame {
    position: absolute;
    left: 22px; top: 30px;
    width: 644px; height: 832px;
    border: 3px solid var(--rule);
    opacity: 0.85;
  }
  .block { position: absolute; left: 0; width: 100%; }
  .festival-title { top: 50px; font-size: 97px; line-height: 1; letter-spacing: 1px; }
  .festival-sub { top: 145px; font-size: 32px; line-height: 1; }
  .credits { top: 182px; font-size: 32px; line-height: 35px; color: var(--ink-soft); }
  .shorts-art {
    position: absolute;
    left: 277px; top: 253px;
    width: 140px; height: 182px;
    background: var(--art);
    border-radius: 6px;
  }
  .divider {
    position: absolute;
    left: 157px; width: 375px; height: 9px;
    background: var(--ink);
  }
  .divider--top { top: 445px; }
  .divider--bottom { top: 697px; }
  .play-list { top: 472px; list-style: none; font-size: 38px; line-height: 35.5px; color: var(--ink-soft); }
  .schedule-day { top: 739px; font-size: 38px; line-height: 1; }
  .schedule-dates { top: 768px; font-size: 57px; line-height: 1; }
  .schedule-dates small { font-size: 20px; }
</style>
</head>
<body>
<div class="canvas">
  <div class="mount"></div>
  <section class="poster">
    <div class="poster-frame"></div>
    <h1 class="block festival-title">Kick The Pickle!</h1>
    <p class="block festival-sub">Summer One Act Festival!</p>
    <p class="block credits">6 Original Short Plays<br>By Milo Tennant</p>
    <div class="shorts-art" role="img" aria-label="Line drawing of a pair of cargo shorts"></div>
    <div class="divider divider--top"></div>
    <ul class="block play-list">
      <li>Tentaxi</li>
      <li>Wine Without Dread</li>
      <li>That Huge Dumb Gothic Epic</li>
      <li>Tune Tickle</li>
      <li>Freshman Fumbles</li>
      <li>Somebody Wore a Hat</li>
    </ul>
    <div class="divider divider--bottom"></div>
    <p class="block schedule-day">Friday Evenings</p>
    <p class="block schedule-dates">July 22<small>ND</small> - August 15<small>TH</small></p>
  </section>
</div>
</body>
</html>
```